Bookmark Design

We would like to design a book mark with logos of our two business and a quote.

One side with the quote "The first wealth is health" - Tobias Quill Harrow and the two logos.

The back side has the two logos with its respective phone numbers and a common address (this is to be advised to the winner of the project).

```html
<!DOCTYPE html>
<html lang="en">
<head>
<meta charset="utf-8">
<title>Bookmark – The first wealth is health</title>
<link href="https://fonts.googleapis.com/css2?family=Fraunces:opsz,wght@9..144,600&family=Red+Hat+Display:ital,wght@0,400;0,700;1,500&display=swap" rel="stylesheet">
<style>
  :root {
    --page: #ffffff;
    --blue: #0457a5;
    --blue-soft: #3f7fc0;
    --green: #6ab66a;
    --white: #ffffff;
    --ink: #1f1f1f;
  }
  html, body {
    margin: 0;
    width: 1200px;
    height: 562px;
    overflow: hidden;
    background: var(--page);
  }
  .bookmark {
    position: absolute;
    left: 184px;
    top: 143px;
    width: 839px;
    height: 279px;
    overflow: hidden;
    background: var(--white);
  }
  .bookmark__shapes {
    position: absolute;
    inset: 0;
  }
  .quote {
    position: absolute;
    left: 76px;
    top: 0;
    margin: 0;
    color: var(--white);
    font-family: "Fraunces", Georgia, serif;
    font-weight: 600;
  }
  .quote__lead {
    position: absolute;
    left: 0;
    top: 55px;
    font-size: 34px;
    line-height: 1;
    white-space: nowrap;
    letter-spacing: -0.3px;
  }
  .quote__main {
    position: absolute;
    left: -2px;
    top: 88px;
    font-size: 86px;
    line-height: 1;
    white-space: nowrap;
    letter-spacing: -0.5px;
  }
  .quote__author {
    position: absolute;
    left: 76px;
    top: 173px;
    margin: 0;
    color: var(--white);
    font-family: "Red Hat Display", Arial, sans-serif;
    font-style: italic;
    font-weight: 500;
    font-size: 15px;
    white-space: nowrap;
  }
  .tagline {
    position: absolute;
    left: 75px;
    top: 254px;
    margin: 0;
    color: var(--ink);
    font-family: "Red Hat Display", Arial, sans-serif;
    font-size: 12.5px;
    white-space: nowrap;
  }
  .brand {
    position: absolute;
    color: var(--white);
    font-family: "Red Hat Display", Arial, sans-serif;
    font-weight: 700;
    text-align: center;
    line-height: 1.1;
  }
  .brand--clinic {
    left: 571px;
    top: 170px;
    width: 110px;
    font-size: 12px;
  }
  .brand__mark {
    display: block;
    width: 50px;
    height: 50px;
    margin: 0 auto 8px;
    border: 2.5px solid var(--white);
    border-radius: 50%;
    box-sizing: border-box;
  }
  .brand--dental {
    left: 700px;
    top: 198px;
    width: 110px;
    font-size: 17px;
    letter-spacing: 0.5px;
  }
</style>
</head>
<body>
  <section class="bookmark">
    <svg class="bookmark__shapes" width="839" height="279" viewBox="0 0 839 279" aria-hidden="false">
      <defs>
        <radialGradient id="foliage-glow" cx="0.3" cy="0.5" r="0.7">
          <stop offset="0" stop-color="var(--blue-soft)" stop-opacity="0.45"/>
          <stop offset="1" stop-color="var(--blue-soft)" stop-opacity="0"/>
        </radialGradient>
        <clipPath id="blue-clip">
          <path d="M0,0 H485 C440,50 418,95 423,140 C428,180 445,210 468,243 H40 C22,243 10,246 0,251 Z"/>
        </clipPath>
      </defs>
      <path class="panel-blue" fill="var(--blue)"
            d="M0,0 H485 C440,50 418,95 423,140 C428,180 445,210 468,243 H40 C22,243 10,246 0,251 Z"/>
      <rect clip-path="url(#blue-clip)" x="0" y="0" width="300" height="279"
            fill="url(#foliage-glow)" role="img" aria-label="Faint leaf foliage decoration"/>
      <path class="panel-green" fill="var(--green)"
            d="M503,0 H839 V279 H525 C482,212 462,160 470,112 C476,72 496,40 503,0 Z"/>
    </svg>

    <h1 class="quote">
      <span class="quote__lead">The first wealth</span>
      <span class="quote__main">is health</span>
    </h1>
    <p class="quote__author">- Tobias Quill Harrow</p>
    <p class="tagline">Lorem ipsum dolor sit amet. Rebum invidunt</p>

    <div class="brand brand--clinic">
      <span class="brand__mark"></span>
      NORTHVALE CLINIC
    </div>
    <div class="brand brand--dental">BAYSIDE<br>DENTAL</div>
  </section>
</body>
</html>
```